Business Card for Quillmark Ledger - A cannabis publication for executives.

I'd like some business cards for Quillmark Ledger. The logo is done (great job!) and I need a card design I will use with PRINTLY. I made it a short project to allow time for printing before an event. These will be standard sized cards (final artwork size 3.66" x 2.16" at 300dpi) with a final card size of 3.5" x 2.0". (See PRINTLY.com if you need more info.) I might try rounded corners but am not sure yet. I think the design will work okay with rounded.

Quillmark Ledger will be a bi-weekly publication for the cannabis industry. It is targeted to investors and industry executives, not consumers or pot smokers. So our market is more B2B. However I am open to creativity and making the card something people remark on.

My contact for card:

Dana Merrow
Founder/CEO
dana@quillmarkledger.example

2740 Harlow Avenue
Boston MA 02135
(617)555-0194

Target Market(s)

Executives, Industry people and investors in the Cannabis sector.

Contact Information for Business Card

PRINTLY does do double sided and the second side can be the same or different images. Only one side is required but use of the second side would be a bonus.

Font styles to use
Serif
Sans Serif
Decorative

Colors

Designer to choose colors to be used in the design.

Requirements
Must have
• Logo, contact info
Nice to have
• Style and design to make the card stand out in a crowd.

```html
<!DOCTYPE html>
<html lang="en">
<head>
<meta charset="utf-8">
<title>Quillmark Ledger – Business Card</title>
<link href="https://fonts.googleapis.com/css2?family=Open+Sans:wght@400;600;700&display=swap" rel="stylesheet">
<style>
  :root {
    --stage: #000000;
    --card-blue: #1077be;
    --card-green: #84ae35;
    --ink-light: #ffffff;
  }
  * { margin: 0; padding: 0; box-sizing: border-box; }
  html, body {
    width: 1200px;
    height: 900px;
    overflow: hidden;
    background: var(--stage);
    font-family: "Open Sans", Arial, sans-serif;
    color: var(--ink-light);
  }
  .stage { position: relative; width: 1200px; height: 900px; }

  .card {
    position: absolute;
    top: 275px;
    width: 477px;
    height: 293px;
    overflow: hidden;
  }
  .card--front {
    left: 116px;
    background: var(--card-blue);
    border-radius: 0 52px 0 52px;
  }
  .card--back {
    left: 622px;
    background: var(--card-green);
    border-radius: 52px 0 52px 0;
  }

  .contact-name {
    position: absolute;
    left: 26px;
    top: 21px;
    font-size: 17px;
    font-weight: 700;
    letter-spacing: -0.2px;
  }
  .contact-role {
    position: absolute;
    left: 26px;
    top: 46px;
    font-size: 12.5px;
    font-weight: 400;
  }

  .brand-name {
    position: absolute;
    font-weight: 600;
    color: var(--ink-light);
    white-space: nowrap;
    letter-spacing: -0.5px;
  }
  .card--front .brand-name {
    left: 28px;
    top: 102px;
    font-size: 33px;
  }
  .card--back .brand-name {
    right: 53px;
    top: 204px;
    font-size: 37px;
  }

  .contact-list {
    position: absolute;
    left: 28px;
    top: 186px;
    list-style: none;
    font-size: 13px;
    line-height: 20px;
  }
  .contact-list li { display: flex; align-items: center; gap: 5px; }
  .contact-list .icon { width: 10px; height: 10px; fill: var(--ink-light); }
  .contact-list .address { margin-top: 5px; }
</style>
</head>
<body>
  <main class="stage">
    <section class="card card--front" aria-label="Business card front">
      <p class="contact-name">Dana Merrow</p>
      <p class="contact-role">Founder/CEO</p>
      <p class="brand-name">Quillmark Ledger</p>
      <ul class="contact-list">
        <li>
          <svg class="icon" viewBox="0 0 24 24" aria-hidden="true"><path d="M6.6 10.8a15.1 15.1 0 0 0 6.6 6.6l2.2-2.2c.3-.3.7-.4 1-.2 1.1.4 2.3.6 3.6.6.6 0 1 .4 1 1V20c0 .6-.4 1-1 1A17 17 0 0 1 3 4c0-.6.4-1 1-1h3.5c.6 0 1 .4 1 1 0 1.3.2 2.5.6 3.6.1.3 0 .7-.2 1z"/></svg>
          <span>(617)555-0194</span>
        </li>
        <li>
          <svg class="icon" viewBox="0 0 24 24" aria-hidden="true"><path d="M2 5h20v14H2z M2 5l10 7 10-7" /><path d="M3 6l9 6.3L21 6v-.5H3z" fill="var(--card-blue)"/></svg>
          <span>dana@quillmarkledger.example</span>
        </li>
        <li class="address">2740 Harlow Avenue&nbsp; Boston MA 02135</li>
      </ul>
    </section>

    <section class="card card--back" aria-label="Business card back">
      <p class="brand-name">Quillmark Ledger</p>
    </section>
  </main>
</body>
</html>
```